Hollybrook Hounds Jamboree Sponsor & Stallholder Leaflet Design

Hollybrook Hounds Jamboree is the updated and refreshed version of the Pemberly Canine Fete (See www.pemberlycaninefete.co.uk).
Under new management, we need a leaflet designed to promote the event to potential stallholders and sponsors.
Hollybrook Hounds Jamboree is a fun day out for dogs and their human companions, with a range of activities for both.
As this is an outdoor event, we would like this theme in the leaflet.
It is being held in the grounds of Thistlecombe Grange - http://www.thistlecombegrange.com
Note:
Leaflet format of DL/6 page is preferred, but will accept A5/4page
I will require the final work in InDesign format
Target Market(s)
Dog owners and lovers
Industry/Entity Type
Event
Look and feel
Each slider illustrates characteristics of the customer's brand and the style your logo design should communicate.

```html
<!DOCTYPE html>
<html lang="en">
<head>
<meta charset="utf-8">
<title>Hollybrook Hounds Jamboree – Sponsor &amp; Stallholder Leaflet</title>
<link rel="stylesheet" href="https://fonts.googleapis.com/css2?family=Roboto+Condensed:wght@400;700&family=Archivo+Narrow:wght@400;600&family=Crimson+Text:wght@600&display=swap">
<style>
:root{
  --stage:#141414;
  --navy:#0b3f86;
  --royal:#0f5cb0;
  --sky:#1a9ee0;
  --pale:#d8edfb;
  --heading:#1576c8;
  --orange:#e2561f;
  --red:#d9261c;
  --purple:#7b3a8f;
  --green:#7cbf2e;
  --white:#ffffff;
  --ink:#2b2b2b;
  --body:"Archivo Narrow", "Arial Narrow", sans-serif;
  --head:"Roboto Condensed", "Arial Narrow", sans-serif;
}
*{box-sizing:border-box;margin:0;padding:0}
html,body{width:900px;height:1200px;overflow:hidden;background:var(--stage)}
body{position:relative;font-family:var(--body);color:var(--ink)}
.spread{position:absolute;left:114px;width:672px;height:516px;overflow:hidden;box-shadow:0 6px 18px rgba(0,0,0,.6)}
.spread--outer{top:72px}
.spread--inner{top:612px}
.page{position:absolute;top:0;width:336px;height:516px;overflow:hidden}
.page--left{left:0}
.page--right{left:336px}
.abs{position:absolute}
.photo{position:absolute}
h2,h3,h4{font-family:var(--head);font-weight:700}
p,li,td{font-size:7.6px;line-height:1.38}
ul{list-style:none}

/* back cover */
.back{background:linear-gradient(#d8edfb 0%,#cfe7fa 60%,#0f5cb0 72%,#0b3f86 100%)}
.back .photo--house{left:0;top:0;width:336px;height:78px;background:linear-gradient(#9bb7c9,#8b6a45 55%,#5d7a3a)}
.tag-box{left:179px;top:52px;width:123px;height:76px;background:var(--orange);border-radius:4px;color:var(--white);font-family:var(--head);font-weight:700;font-size:16.5px;line-height:1.12;text-align:center;padding-top:7px}
.section-head{color:var(--heading);font-size:13px}
.back .section-head{left:29px}
.back p{color:var(--ink);text-align:justify}
.price-table{left:29px;top:162px;width:275px;border-collapse:collapse}
.price-table th{font-family:var(--body);font-weight:400;font-size:7.4px;background:var(--royal);color:var(--white);text-align:left;padding:1px 6px;height:12px}
.price-table td{font-size:7.4px;height:12px;padding:0 6px;border-top:1px solid var(--white)}
.price-table td:first-child{background:transparent;width:86px;padding-left:0}
.price-table tbody tr:nth-child(odd) td+td{background:#bfe0f7}
.price-table tbody tr:nth-child(even) td+td{background:#e8f4fc}
.price-table td+td{border-left:1px solid var(--white)}
.contact-label{left:29px;top:387px;width:103px;text-align:right;color:var(--white);font-family:var(--head);font-size:7.8px;line-height:1.5}
.contact-list{left:144px;top:383px}
.contact-list li{display:flex;align-items:center;gap:6px;color:var(--white);font-family:var(--head);font-weight:700;font-size:10px;line-height:15px}
.contact-list svg{width:9px;height:9px}
.organiser{left:0;top:440px;width:336px;text-align:center;color:var(--white);font-family:var(--head)}
.organiser .lead{font-size:9.5px;font-weight:700}
.organiser .company{font-size:21px;font-weight:700;color:#aee0ff;line-height:1.15}
.organiser .addr{font-size:9px;font-weight:700;line-height:1.35}

/* front cover */
.front{background:var(--royal)}
.title{right:23px;top:26px;font-family:"Crimson Text",serif;font-weight:600;font-size:25px;color:var(--white)}
.front .photo--estate{left:0;top:62px;width:336px;height:290px;background:linear-gradient(#b7c4cf 0%,#d2d6d8 30%,#9a5a3c 55%,#6e8a3f 75%,#5f8a36 100%)}
.dog-shot{background:linear-gradient(#7ea856,#b08a55);border:4px solid var(--white);box-shadow:0 2px 4px rgba(0,0,0,.35)}
.date-badge{left:203px;top:195px;width:68px;height:68px;border-radius:50%;background:var(--royal);border:3px solid var(--white);color:var(--white);font-family:var(--head);font-weight:700;font-size:12px;line-height:1.3;text-align:center;display:flex;align-items:center;justify-content:center}
.cover-strap{right:38px;top:301px;text-align:right;color:var(--white);font-family:var(--head);font-weight:700;font-size:13px;line-height:1.35;text-shadow:0 1px 2px rgba(0,0,0,.5)}
.front .story{left:22px;top:349px;width:292px;color:var(--white)}
.front .story p{text-align:justify;margin-bottom:10px}

/* inside left */
.inside-l{background:var(--white)}
.inside-l .section-head{left:23px;color:var(--heading)}
.inside-l p{left:23px;width:293px;text-align:justify}
.inside-l .photo--grounds{left:0;top:192px;width:336px;height:190px;border-top-right-radius:28px;background:linear-gradient(120deg,#7f9a6a,#b9c79a 45%,#6f8c4b 70%,#9aa56c)}
.promo-box{left:128px;top:246px;width:162px;height:84px;background:rgba(70,60,55,.72);border-radius:8px;color:var(--white);padding:7px 10px}
.promo-box h4{font-size:12px;margin-bottom:3px}
.promo-box li,.bullets li{font-size:7.6px;line-height:1.3}
.promo-box li::before,.bullets li::before{content:"• "}
.sponsor-band{left:0;top:355px;width:336px;height:161px}
.sponsor-tag{left:115px;top:367px;width:109px;height:25px;background:var(--red);color:var(--white);font-family:var(--head);font-weight:700;font-size:13px;text-align:center;line-height:25px;border-radius:3px 3px 0 0}
.inside-l .why{left:23px;top:388px;color:#a9dcff;font-size:13px}
.bullets{left:23px;top:407px;color:var(--white)}
.inside-l .give{left:23px;top:471px;color:#a9dcff;font-size:13px}
.inside-l .give-text{left:23px;top:487px;color:var(--white);width:300px}

/* inside right */
.inside-r{background:var(--sky)}
.card{position:absolute;border-radius:6px;color:var(--white);padding:6px 12px}
.card h3{font-size:12.5px;line-height:1.15;margin-bottom:3px}
.card li{font-size:7.2px;line-height:1.38;display:flex;gap:4px;align-items:flex-start}
.card li svg{flex:none;width:6px;height:6px;margin-top:2px}
.card--main{left:29px;top:22px;width:279px;height:123px;background:#1c82cc}
.card--trade{left:29px;top:246px;width:279px;height:217px;background:#1c82cc;border-radius:0 6px 6px 6px}
.card--ring{left:29px;top:150px;width:137px;height:92px;background:var(--purple);padding:6px 10px}
.card--comp{left:170px;top:150px;width:138px;height:63px;background:#1a6ebc;padding:6px 10px}
.card--gift{left:170px;top:216px;width:138px;height:82px;background:var(--orange);padding:5px 9px}
.card--gift h3{font-size:12px;margin-bottom:2px}
.card--gift li{font-size:7px;line-height:1.3}
.trade-head{left:42px;top:318px;font-size:17px;color:var(--white)}
.trade-text{left:42px;top:341px;width:262px;color:var(--white);text-align:justify}
.space-table{left:42px;top:382px;width:137px;border-collapse:collapse}
.space-table th{background:var(--red);color:var(--white);font-family:var(--head);font-size:7.8px;height:13px}
.space-table td{height:12.5px;font-size:7.8px;padding:0 6px;border-top:1px solid var(--white);color:var(--white)}
.space-table td:first-child{background:var(--green);color:#0b3f86}
.space-table td+td{background:var(--navy);text-align:right;font-weight:600;border-left:2px solid var(--white)}
.notes{left:29px;top:469px;width:286px;color:var(--white);font-size:7.6px}
</style>
</head>
<body>

<!-- OUTER SPREAD -->
<section class="spread spread--outer">

  <article class="page page--left back">
    <div class="photo photo--house" role="img" aria-label="Photograph of the country house and its front lawn"></div>
    <svg class="abs" style="left:0;top:52px" width="336" height="40" viewBox="0 0 336 40" aria-hidden="true">
      <path d="M0 18 C80 2 150 34 336 10 L336 40 L0 40Z" fill="#d8edfb"/>
      <path d="M0 18 C80 2 150 34 336 10" stroke="#0f5cb0" stroke-width="4" fill="none"/>
      <path d="M0 24 C90 10 160 38 336 16" stroke="#5bb5ea" stroke-width="2" fill="none"/>
    </svg>
    <div class="abs tag-box">Additional<br>Marketing<br>Opportunities</div>

    <h2 class="abs section-head" style="top:128px">Show Guide</h2>
    <p class="abs" style="left:29px;top:139px;width:275px">A minimum of 32 pages, the show guide not only contains useful features and stories, but also a full listing of all sponsors and exhibitors.</p>

    <table class="abs price-table">
      <thead><tr><th style="background:transparent"></th><th>Exhibitor</th><th>Standard Advertiser</th></tr></thead>
      <tbody>
        <tr><td>Back cover</td><td>£350</td><td>£700</td></tr>
        <tr><td>Full page</td><td>£250</td><td>£500</td></tr>
        <tr><td>Half Page</td><td>£135</td><td>£2700</td></tr>
        <tr><td>Quarter Page</td><td>£75</td><td>£150</td></tr>
        <tr><td>Sixth Page</td><td>£50</td><td>£100</td></tr>
      </tbody>
    </table>

    <h2 class="abs section-head" style="top:245px">Promotional Voucher</h2>
    <p class="abs" style="left:29px;top:257px;width:275px">The centre of the guide will contain a pull out voucher booklet, with 6 vouchers per page. Exhibitors offering a special promotion, price or service during the event can promote it via a voucher, which will not only highlight the offer, but also identify the location of their stand. This costs £50 per voucher Banners in Competition Rings - £10 per meter (60cm high) - design &amp; production not included.</p>

    <svg class="abs" style="left:0;top:318px" width="336" height="60" viewBox="0 0 336 60" aria-hidden="true">
      <path d="M0 10 C90 30 200 -4 336 22 L336 60 L0 60Z" fill="#0f5cb0"/>
      <path d="M0 10 C90 30 200 -4 336 22" stroke="#e8566b" stroke-width="3" fill="none"/>
      <path d="M0 18 C90 38 200 4 336 30" stroke="#ffffff" stroke-width="3" fill="none"/>
      <path d="M0 26 C100 44 210 12 336 36 L336 60 L0 60Z" fill="#0b4a98"/>
    </svg>

    <div class="abs contact-label">To book or for more information contact the Hollybrook Hounds Jamboree team:</div>
    <ul class="abs contact-list">
      <li><svg viewBox="0 0 10 10"><rect width="10" height="10" rx="2" fill="#f39a1e"/><path d="M2.5 3.2c1 2.4 2 3.4 4.3 4.3l.9-1-1.4-.9-.6.6C4.9 5.8 4.4 5.2 4 4.4l.6-.6-.9-1.4z" fill="#fff"/></svg>01632 960418</li>
      <li><svg viewBox="0 0 10 10"><rect width="10" height="10" rx="2" fill="#f39a1e"/><circle cx="5" cy="5" r="2.4" fill="none" stroke="#fff" stroke-width="1"/></svg>contact@hollybrookhounds.co.uk</li>
      <li><svg viewBox="0 0 10 10"><rect width="10" height="10" rx="2" fill="#f39a1e"/><circle cx="5" cy="5" r="2.8" fill="none" stroke="#fff" stroke-width=".9"/><path d="M2.2 5h5.6M5 2.2v5.6" stroke="#fff" stroke-width=".7"/></svg>www.hollybrookhounds.co.uk</li>
    </ul>

    <div class="abs organiser">
      <div class="lead">This event is organised &amp; managed by</div>
      <div class="company">Marlow Events Ltd</div>
      <div class="addr">22 Larkspur Lane, Little Ashby<br>Wexham, WX4 7RT</div>
    </div>
  </article>

  <article class="page page--right front">
    <div class="photo photo--estate" role="img" aria-label="Photograph of the country house with cloudy sky and lawn"></div>
    <svg class="abs" style="left:0;top:0" width="336" height="100" viewBox="0 0 336 100" aria-hidden="true">
      <path d="M0 0 H336 V78 C250 92 160 50 0 72Z" fill="#0f5cb0"/>
      <path d="M0 72 C160 50 250 92 336 78" stroke="#ffffff" stroke-width="3" fill="none"/>
      <path d="M0 80 C160 58 250 100 336 86" stroke="#5bb5ea" stroke-width="2" fill="none"/>
    </svg>
    <div class="abs title">Pemberly Canine Fete</div>

    <div class="photo dog-shot" role="img" aria-label="Photo of a terrier on grass" style="left:156px;top:166px;width:64px;height:64px;transform:rotate(-6deg)"></div>
    <div class="photo dog-shot" role="img" aria-label="Photo of a terrier looking up" style="left:248px;top:162px;width:66px;height:64px;transform:rotate(5deg)"></div>
    <div class="photo dog-shot" role="img" aria-label="Photo of a terrier sitting" style="left:168px;top:236px;width:66px;height:62px;transform:rotate(-3deg)"></div>
    <div class="photo dog-shot" role="img" aria-label="Photo of a terrier standing" style="left:245px;top:232px;width:72px;height:66px;transform:rotate(4deg)"></div>
    <div class="abs date-badge">27th &amp; 28th<br>July 2013</div>

    <svg class="abs" style="left:0;top:326px" width="336" height="50" viewBox="0 0 336 50" aria-hidden="true">
      <path d="M0 22 C110 4 230 8 336 26 L336 50 L0 50Z" fill="#0f5cb0"/>
      <path d="M0 22 C110 4 230 8 336 26" stroke="#d9261c" stroke-width="3" fill="none"/>
      <path d="M0 15 C110 -3 230 1 336 19" stroke="#f08a2c" stroke-width="2" fill="none"/>
    </svg>

    <div class="abs cover-strap">Sponsorship &amp; Trade<br>Exhibitor Opportunities</div>

    <div class="abs story">
      <p>Pemberly Canine Fete was created and launched in 2009, in aid of Aid for Servicemen, co-inciding with the deployment of the Light Horse Regiment on active service to Afghanistan. Parents left behind during their deployment where amongst the committed volunteers who participated and helped in the organisation of the event. The event captured the animal loving spirit of Wexham at a point when the whole county was passionate in their support of 'our blokes doing their bit' in Afghanistan. Expecting a few hundred dogs and 5,000 humans, it actual attracted circa 1,000 dogs, with almost 15,000 guests, the inaugural event was seen as an outstanding success. 2010 saw a visitor increase of circa 20%.</p>
      <p>Due to the overwhelming footfall, 2013 will become a two day event and is now known as 'Hollybrook Hounds Jamboree'.</p>
    </div>
  </article>
</section>

<!-- INNER SPREAD -->
<section class="spread spread--inner">

  <article class="page page--left inside-l">
    <h2 class="abs section-head" style="top:23px">Where Is It Held?</h2>
    <p class="abs" style="top:38px">Thistlecombe Grange is one of Wexham's most romantic and impressive large Edwardian country houses set in sweeping parkland. It was built to a grand design by Henry Albert Fenwick, grandson of Henry Fenwick, a pioneer of modern holiday travel, and is lived in today by his descendants. Although a private family home, and not open to the public, Thistlecombe Grange offers a unique and magical venue for the Pemberly Canine Fete.</p>
    <p class="abs" style="top:100px">Near Ashby Market, in North Wexham, Thistlecombe Grange is approximately 30 minutes from Wexham City.</p>

    <h2 class="abs section-head" style="top:129px">Who Will Attend?</h2>
    <p class="abs" style="top:144px">The target audience for this event is anyone who likes, owns or has an interest in dogs! Heavily promoted to dog lovers and owners, across several mediums, it attracts visitors of all ages across the demographic spectrum.</p>

    <div class="photo photo--grounds" role="img" aria-label="Soft-focus photograph of a garden pavilion among trees"></div>
    <div class="abs promo-box">
      <h4>How Will It Be Promoted</h4>
      <ul>
        <li>Dedicated website</li>
        <li>Social Media - Pawbook, Chirper etc</li>
        <li>Regional Advertising</li>
        <li>Dog &amp; pet Press</li>
        <li>Regional Radio</li>
        <li>Regional database via email</li>
      </ul>
    </div>

    <svg class="abs sponsor-band" viewBox="0 0 336 161" aria-hidden="true">
      <path d="M0 30 C80 4 200 6 336 20 L336 161 L0 161Z" fill="#0f5cb0"/>
      <path d="M0 30 C80 4 200 6 336 20" stroke="#5bb5ea" stroke-width="3" fill="none"/>
      <path d="M0 60 C120 40 220 44 336 56 L336 161 L0 161Z" fill="#0e57a8"/>
    </svg>
    <div class="abs sponsor-tag">SPONSORSHIP</div>

    <h3 class="abs why">Why sponsor</h3>
    <ul class="abs bullets">
      <li>Give your brands or products exposure to circa 20,000 visitors</li>
      <li>Access a highly targeted market</li>
      <li>Lead generation</li>
      <li>Brand positioning</li>
      <li>Increase brand recognition</li>
    </ul>
    <h3 class="abs give">What Does Sponsorship Give You?</h3>
    <p class="abs give-text">There are four types of sponsorship, dependant of your budget and marketing goals.</p>
  </article>

  <article class="page page--right inside-r">
    <svg width="0" height="0" style="position:absolute" aria-hidden="true">
      <symbol id="tick" viewBox="0 0 6 6"><circle cx="3" cy="3" r="3" fill="#fff"/><path d="M1.6 3.1l1 1 1.8-2" stroke="#1c82cc" stroke-width=".8" fill="none"/></symbol>
    </svg>

    <div class="card card--main">
      <h3>Main Event Sponsor</h3>
      <ul>
        <li><svg><use href="#tick"/></svg>Branding on all media communications - leaflets, tickets, website, emails etc</li>
        <li><svg><use href="#tick"/></svg>Large Exhibition Space</li>
        <li><svg><use href="#tick"/></svg>Sign and Banner Rights across the event venue and rings (banner production included)</li>
        <li><svg><use href="#tick"/></svg>Local, regional and national Media Exposure</li>
        <li><svg><use href="#tick"/></svg>2 pages in the show guide</li>
        <li><svg><use href="#tick"/></svg>Global Judging rights</li>
        <li><svg><use href="#tick"/></svg>Massive Consumer Awareness</li>
        <li><svg><use href="#tick"/></svg>20 Complimentary tickets</li>
      </ul>
    </div>

    <div class="card card--trade"></div>

    <div class="card card--ring">
      <h3>Ring Sponsor</h3>
      <ul>
        <li><svg><use href="#tick"/></svg>Exhibition Space</li>
        <li><svg><use href="#tick"/></svg>Joint Banner Rights in the event ring (banner production included)</li>
        <li><svg><use href="#tick"/></svg>1 pages in the show guide</li>
        <li><svg><use href="#tick"/></svg>Ring Judging rights</li>
        <li><svg><use href="#tick"/></svg>5 Complimentary tickets</li>
      </ul>
    </div>

    <div class="card card--comp">
      <h3>Competition Sponsor</h3>
      <ul>
        <li><svg><use href="#tick"/></svg>Exhibition Space</li>
        <li><svg><use href="#tick"/></svg>1/2 page in the show guide</li>
        <li><svg><use href="#tick"/></svg>Competition Judging rights</li>
        <li><svg><use href="#tick"/></svg>2 Complimentary tickets</li>
      </ul>
    </div>

    <div class="card card--gift">
      <h3>Gift/Sample Sponsor</h3>
      <ul>
        <li><svg><use href="#tick"/></svg>Promote your brand or product by supplying gift or sample</li>
        <li><svg><use href="#tick"/></svg>Data collection opportunity</li>
        <li><svg><use href="#tick"/></svg>Exhibition Space</li>
        <li><svg><use href="#tick"/></svg>1/2 page in the show guide</li>
      </ul>
    </div>

    <div class="photo dog-shot" role="img" aria-label="Photo of a terrier standing on grass" style="left:68px;top:253px;width:69px;height:60px;transform:rotate(-2deg)"></div>

    <h2 class="abs trade-head">TRADE EXHIBITORS</h2>
    <p class="abs trade-text">There are several space options available to exhibitors, both covered and grass space only. Covering the two days of the event, exhibitors also get a line listing in the event show guide and website.</p>

    <table class="abs space-table">
      <thead><tr><th colspan="2">GRASS SPACE ONLY</th></tr></thead>
      <tbody>
        <tr><td>3m(w) x 6m(d)</td><td>£150</td></tr>
        <tr><td>6m(w) x 10m(d)</td><td>£250</td></tr>
        <tr><td>9m(w) x 10m(d)</td><td>£350</td></tr>
        <tr><td>12m(w) x 10m(d)</td><td>£450</td></tr>
      </tbody>
    </table>

    <div class="photo dog-shot" role="img" aria-label="Photo of a terrier standing side-on" style="left:198px;top:377px;width:82px;height:78px;transform:rotate(5deg)"></div>

    <p class="abs notes"><b>Notes:</b> All exhibitors must have valid and suitable public, product &amp; employee liability insurance All (human) food based exhibitors must have suitable food hygiene qualifications and certification</p>
  </article>
</section>

</body>
</html>
```